Bramfield Animal Hospital brochure

We have found that our current clients do not know all of the services that we offer so we want to make a hospital brochure to make our services more known. Our website has all of our services listed but we find that clients aren't looking at our website as much as we would like so we are hoping a hospital brochure can sum up our main services and maybe lead to more people visiting our website. Our hospital colors are blue and maroon and our moto is "Outstanding Medicine, Extraordinary Service." Some of the service we would like to promote more include digital x-ray, ultrasounds, echocardiograms, laser therapy and dentals. We also offer after hours emergency care but only to our current clients. You can find more services listed on our website We are in a small town so we want a personal yet professional feel.

Feel free to visit our website to get a better feel for our business https://thecorvelpets.com/

• 6-8 panel brochure
• I included some photos from around the hospital. If you feel that you can make a few work in the brochure then great but don't feel obligated to.

```html
<!DOCTYPE html>
<html lang="en">
<head>
<meta charset="utf-8">
<title>Bramfield Animal Hospital – Brochure</title>
<link rel="stylesheet" href="https://fonts.googleapis.com/css2?family=Open+Sans:ital,wght@0,400;0,600;0,700;1,400&display=swap">
<style>
  :root {
    --maroon: #9e1b22;
    --maroon-dark: #7d1319;
    --maroon-soft: #b8353b;
    --paper: #ffffff;
    --paper-shade: #f3f1f0;
    --ink: #4a4a4a;
    --ink-soft: #7a7a7a;
    --backdrop: #e9e7e4;
    --photo-warm: #c89a6a;
    --photo-grey: #8a8c90;
    --photo-green: #7f9a45;
  }
  * { box-sizing: border-box; margin: 0; padding: 0; }
  html, body { width: 1200px; height: 2400px; overflow: hidden; }
  body {
    background: var(--backdrop);
    font-family: "Open Sans", Arial, sans-serif;
    color: var(--ink);
    display: flex; flex-direction: column; align-items: center; justify-content: center;
    gap: 110px;
  }
  .spread {
    width: 1100px; height: 850px;
    display: grid; grid-template-columns: repeat(3, 1fr);
    background: var(--paper);
    box-shadow: 0 6px 24px rgba(0,0,0,.15);
  }
  .panel { position: relative; overflow: hidden; }
  .panel--maroon { background: var(--maroon); color: #fff; }
  .photo { position: absolute; overflow: hidden; }
  .curve { position: absolute; left: 0; width: 100%; }

  /* brand mark */
  .brand { display: flex; align-items: center; gap: 10px; justify-content: center; }
  .brand__dot { width: 22px; height: 22px; border-radius: 50%; background: var(--maroon); flex: none; }
  .brand__name { font-weight: 600; color: var(--maroon); text-transform: uppercase; letter-spacing: 1px; line-height: 1.15; }

  .head-bar {
    background: var(--maroon); color: #fff; font-weight: 700;
    padding: 6px 18px; border-radius: 0 16px 16px 0; display: inline-block;
  }
  .pill {
    display: inline-flex; align-items: center; gap: 10px;
    background: var(--maroon); color: #fff; font-weight: 700; border-radius: 20px;
    padding: 6px 20px 6px 8px;
  }
  .pill__icon { width: 24px; height: 24px; border-radius: 50%; background: #fff; display: grid; place-items: center; }
  .body-text { font-size: 13px; line-height: 1.6; color: var(--ink); }
  .body-text p + p { margin-top: 10px; }

  /* outside left */
  .emergency { padding: 34px 0 0; }
  .emergency .brand { margin-bottom: 26px; }
  .emergency .brand__name { font-size: 15px; }
  .emergency__title { font-size: 19px; }
  .emergency__sub { font-style: italic; color: var(--ink-soft); font-size: 16px; margin: 10px 28px 14px; }
  .emergency .body-text { margin: 0 28px; }
  .emergency .pill { margin: 20px 28px 0; font-size: 15px; }
  .emergency .photo { left: 0; right: 0; bottom: 0; height: 330px;
    background: radial-gradient(circle at 45% 45%, #c79c73 0 18%, transparent 32%), linear-gradient(180deg, #9ab95a, var(--photo-green) 60%, #5f7a2e); }

  /* outside middle */
  .contact { text-align: center; }
  .contact__map { width: 250px; height: 250px; border-radius: 50%; margin: 40px auto 0;
    background: radial-gradient(circle, #f4f2ef, #dcd9d5); border: 6px solid rgba(255,255,255,.6); }
  .contact__name { margin-top: 40px; font-size: 21px; color: rgba(255,255,255,.55); letter-spacing: 2px; text-transform: uppercase; font-weight: 400; line-height: 1.3; }
  .contact__title { margin-top: 30px; font-size: 30px; font-weight: 700; letter-spacing: .5px; }
  .contact__addr { font-size: 15px; margin-top: 10px; line-height: 1.5; }
  .contact .pill { background: #fff; color: var(--maroon); margin-top: 16px; font-size: 17px; }
  .contact .pill__icon { background: var(--maroon); }
  .contact__lines { margin-top: 14px; font-size: 15px; line-height: 1.7; }

  /* cover */
  .cover .photo { left: 0; right: 0; top: 0; height: 420px;
    background: linear-gradient(120deg, #eceae7 0%, var(--photo-grey) 38%, var(--photo-warm) 62%, #e7e2dc 100%); }
  .cover__badge { position: absolute; left: 50%; top: 360px; transform: translateX(-50%);
    width: 250px; padding-top: 30px; text-align: center; }
  .cover .brand__name { font-size: 24px; }
  .cover__tagline { position: absolute; left: 30px; right: 30px; top: 530px; }
  .cover__title { font-size: 27px; color: var(--maroon); font-weight: 600; letter-spacing: .3px; }
  .cover__sub { font-size: 17px; color: var(--ink-soft); margin-top: 6px; line-height: 1.35; }
  .url-bar { position: absolute; left: 30px; right: 0; bottom: 40px; background: var(--maroon); color: #fff;
    font-size: 18px; font-weight: 600; padding: 9px 22px; border-radius: 22px 0 0 22px; display: flex; align-items: center; gap: 16px; }
  .url-bar__dot { width: 12px; height: 12px; border-radius: 50%; background: #fff; }

  /* inside left */
  .about .photo--main { left: 0; right: 0; top: 0; height: 330px;
    background: linear-gradient(160deg, #dfe3de, #8f8a7e 45%, #c79d68 75%, #e9e4de); }
  .about .photo--inset { width: 120px; height: 120px; border-radius: 50%; left: 210px; top: 250px; border: 5px solid #fff;
    background: radial-gradient(circle, #c98c5c, #8a4b2b); }
  .about__content { position: absolute; top: 400px; left: 0; right: 28px; }
  .about .head-bar { font-size: 17px; margin-bottom: 16px; }
  .about .body-text { margin-left: 28px; }
  .about__lead { font-size: 15px; line-height: 1.5; margin-bottom: 10px; color: var(--ink); }
  .about .pill { position: absolute; left: 28px; bottom: 34px; font-size: 17px; }

  /* services */
  .services { padding: 50px 30px 0; }
  .services__title { font-size: 24px; font-weight: 700; letter-spacing: .5px; margin-bottom: 14px; }
  .services__list { list-style: none; font-size: 15px; line-height: 1.5; }
  .services__list li { display: flex; align-items: center; gap: 9px; }
  .services__list svg { flex: none; }
  .services__thumbs { position: absolute; left: 40px; right: 40px; bottom: 86px; display: flex; justify-content: space-between; }
  .thumb { width: 80px; height: 80px; border-radius: 50%; border: 4px solid #fff;
    background: linear-gradient(140deg, #b7c6c8, #5b7c82); }
  .services__url { position: absolute; left: 30px; right: 30px; bottom: 30px; text-align: center;
    background: #fff; color: var(--maroon); font-size: 17px; font-weight: 600; border-radius: 20px; padding: 7px 0; }

  /* love them all */
  .love { padding-top: 50px; }
  .love .head-bar { font-size: 18px; margin-bottom: 16px; }
  .love .body-text { margin: 0 28px; }
  .love__circles { position: absolute; left: 130px; top: 400px; display: grid; grid-template-columns: 100px 100px; gap: 6px; }
  .love__circle { width: 100px; height: 100px; border-radius: 50%; border: 4px solid #fff; box-shadow: 0 0 0 1px #ddd; }
  .love .photo--main { left: 0; right: 0; bottom: 0; height: 300px;
    background: linear-gradient(150deg, #e4e1dc, #b9a68d 40%, #3f4f7a 70%, #d9d6d2); }
</style>
</head>
<body>

<!-- Outside spread -->
<section class="spread spread--outside">
  <article class="panel emergency">
    <div class="brand"><span class="brand__dot"></span><span class="brand__name">Bramfield<br>Animal Hospital</span></div>
    <h2 class="head-bar emergency__title">24 Hour Emergency Care</h2>
    <p class="emergency__sub">Because minutes can matter</p>
    <div class="body-text">
      <p>We keep a veterinarian on call 24 hours a day for emergency services, so current clients can reach us quickly when it matters most.</p>
      <p>If you are not a current client and need after hours care, please contact the nearest emergency clinic listed below for prompt help.</p>
    </div>
    <div class="pill"><span class="pill__icon"><svg width="14" height="14" viewBox="0 0 24 24"><path fill="#9e1b22" d="M6.6 10.8a15.5 15.5 0 006.6 6.6l2.2-2.2c.3-.3.7-.4 1-.2 1.1.4 2.3.6 3.6.6.6 0 1 .4 1 1V20c0 .6-.4 1-1 1A17 17 0 013 4c0-.6.4-1 1-1h3.5c.6 0 1 .4 1 1 0 1.3.2 2.5.6 3.6.1.3 0 .7-.2 1z"/></svg></span>(802) 555-0148</div>
    <div class="photo" role="img" aria-label="Photo of a spaniel puppy running through a green field"></div>
    <svg class="curve" style="bottom:270px" width="367" height="80" viewBox="0 0 367 80" preserveAspectRatio="none"><path d="M0 0H367V20Q190 10 0 80Z" fill="#fff"/></svg>
  </article>

  <article class="panel panel--maroon contact">
    <div class="contact__map" role="img" aria-label="Street map showing the hospital location"></div>
    <p class="contact__name">Bramfield Animal<br>Hospital</p>
    <h2 class="contact__title">CONTACT US</h2>
    <p class="contact__addr">212 Mill Brook Road<br>Bramfield Vermont, 05099</p>
    <div class="pill"><span class="pill__icon"><svg width="14" height="14" viewBox="0 0 24 24"><path fill="#fff" d="M6.6 10.8a15.5 15.5 0 006.6 6.6l2.2-2.2c.3-.3.7-.4 1-.2 1.1.4 2.3.6 3.6.6.6 0 1 .4 1 1V20c0 .6-.4 1-1 1A17 17 0 013 4c0-.6.4-1 1-1h3.5c.6 0 1 .4 1 1 0 1.3.2 2.5.6 3.6.1.3 0 .7-.2 1z"/></svg></span>(802) 555-0148</div>
    <p class="contact__lines">info@thecorvelpets.com<br>www.thecorvelpets.com</p>
  </article>

  <article class="panel cover">
    <div class="photo" role="img" aria-label="Photo of a golden retriever resting its head on a grey cat"></div>
    <svg class="curve" style="top:330px" width="367" height="100" viewBox="0 0 367 100" preserveAspectRatio="none"><path d="M0 100V40Q183 -30 367 40V100Z" fill="#fff"/></svg>
    <div class="cover__badge"><div class="brand"><span class="brand__dot"></span><span class="brand__name">Bramfield<br>Animal Hospital</span></div></div>
    <div class="cover__tagline">
      <h1 class="cover__title">EVERY PATIENT, EVERY TIME</h1>
      <p class="cover__sub">The care you would want for any member of your family.</p>
    </div>
    <div class="url-bar"><span class="url-bar__dot"></span>www.thecorvelpets.com</div>
  </article>
</section>

<!-- Inside spread -->
<section class="spread spread--inside">
  <article class="panel about">
    <div class="photo photo--main" role="img" aria-label="Photo of the veterinarian sitting outdoors with two dogs"></div>
    <svg class="curve" style="top:280px" width="367" height="60" viewBox="0 0 367 60" preserveAspectRatio="none"><path d="M0 60V10Q200 50 367 0V60Z" fill="#fff"/></svg>
    <div class="photo photo--inset" role="img" aria-label="Portrait photo of a staff member"></div>
    <div class="about__content">
      <h2 class="head-bar">Bramfield Animal Hospital</h2>
      <div class="body-text">
        <p class="about__lead">Outstanding medicine, extraordinary services. We care for dogs, cats, birds, small animals, and other exotic pets.</p>
        <p>We believe in building something special. Taking care of you and your pet like family is the only way we know how to live. In order to do that, we take the time to listen. To connect. To understand. And to teach.</p>
        <p>We believe that veterinary care is at its best when it involves you, and your deeper concerns or goals for your pet are addressed. We are a hospital for you and your companion.</p>
      </div>
    </div>
    <div class="pill"><span class="pill__icon"><svg width="14" height="14" viewBox="0 0 24 24"><path fill="#9e1b22" d="M6.6 10.8a15.5 15.5 0 006.6 6.6l2.2-2.2c.3-.3.7-.4 1-.2 1.1.4 2.3.6 3.6.6.6 0 1 .4 1 1V20c0 .6-.4 1-1 1A17 17 0 013 4c0-.6.4-1 1-1h3.5c.6 0 1 .4 1 1 0 1.3.2 2.5.6 3.6.1.3 0 .7-.2 1z"/></svg></span>(802) 555-0148</div>
  </article>

  <article class="panel panel--maroon services">
    <h2 class="services__title">OUR SERVICES</h2>
    <ul class="services__list">
      <li><svg width="13" height="13" viewBox="0 0 16 16"><circle cx="8" cy="8" r="7" fill="none" stroke="#fff" stroke-width="1.4"/><path d="M4.5 8.2l2.3 2.3 4.7-4.7" fill="none" stroke="#fff" stroke-width="1.6"/></svg>Allergy and Dermatology Testing</li>
      <li><svg width="13" height="13" viewBox="0 0 16 16"><circle cx="8" cy="8" r="7" fill="none" stroke="#fff" stroke-width="1.4"/><path d="M4.5 8.2l2.3 2.3 4.7-4.7" fill="none" stroke="#fff" stroke-width="1.6"/></svg>Avian Care</li>
      <li><svg width="13" height="13" viewBox="0 0 16 16"><circle cx="8" cy="8" r="7" fill="none" stroke="#fff" stroke-width="1.4"/><path d="M4.5 8.2l2.3 2.3 4.7-4.7" fill="none" stroke="#fff" stroke-width="1.6"/></svg>Blood Tests and Urine Screening</li>
      <li><svg width="13" height="13" viewBox="0 0 16 16"><circle cx="8" cy="8" r="7" fill="none" stroke="#fff" stroke-width="1.4"/><path d="M4.5 8.2l2.3 2.3 4.7-4.7" fill="none" stroke="#fff" stroke-width="1.6"/></svg>Canine and Feline Dental Care</li>
      <li><svg width="13" height="13" viewBox="0 0 16 16"><circle cx="8" cy="8" r="7" fill="none" stroke="#fff" stroke-width="1.4"/><path d="M4.5 8.2l2.3 2.3 4.7-4.7" fill="none" stroke="#fff" stroke-width="1.6"/></svg>Cardiology Care</li>
      <li><svg width="13" height="13" viewBox="0 0 16 16"><circle cx="8" cy="8" r="7" fill="none" stroke="#fff" stroke-width="1.4"/><path d="M4.5 8.2l2.3 2.3 4.7-4.7" fill="none" stroke="#fff" stroke-width="1.6"/></svg>Cold Laser Therapy</li>
      <li><svg width="13" height="13" viewBox="0 0 16 16"><circle cx="8" cy="8" r="7" fill="none" stroke="#fff" stroke-width="1.4"/><path d="M4.5 8.2l2.3 2.3 4.7-4.7" fill="none" stroke="#fff" stroke-width="1.6"/></svg>Digital X-Ray</li>
      <li><svg width="13" height="13" viewBox="0 0 16 16"><circle cx="8" cy="8" r="7" fill="none" stroke="#fff" stroke-width="1.4"/><path d="M4.5 8.2l2.3 2.3 4.7-4.7" fill="none" stroke="#fff" stroke-width="1.6"/></svg>Emergency Care</li>
      <li><svg width="13" height="13" viewBox="0 0 16 16"><circle cx="8" cy="8" r="7" fill="none" stroke="#fff" stroke-width="1.4"/><path d="M4.5 8.2l2.3 2.3 4.7-4.7" fill="none" stroke="#fff" stroke-width="1.6"/></svg>End of Life Care</li>
      <li><svg width="13" height="13" viewBox="0 0 16 16"><circle cx="8" cy="8" r="7" fill="none" stroke="#fff" stroke-width="1.4"/><path d="M4.5 8.2l2.3 2.3 4.7-4.7" fill="none" stroke="#fff" stroke-width="1.6"/></svg>Exotic Pet Care</li>
      <li><svg width="13" height="13" viewBox="0 0 16 16"><circle cx="8" cy="8" r="7" fill="none" stroke="#fff" stroke-width="1.4"/><path d="M4.5 8.2l2.3 2.3 4.7-4.7" fill="none" stroke="#fff" stroke-width="1.6"/></svg>Eye Care</li>
      <li><svg width="13" height="13" viewBox="0 0 16 16"><circle cx="8" cy="8" r="7" fill="none" stroke="#fff" stroke-width="1.4"/><path d="M4.5 8.2l2.3 2.3 4.7-4.7" fill="none" stroke="#fff" stroke-width="1.6"/></svg>House Calls</li>
      <li><svg width="13" height="13" viewBox="0 0 16 16"><circle cx="8" cy="8" r="7" fill="none" stroke="#fff" stroke-width="1.4"/><path d="M4.5 8.2l2.3 2.3 4.7-4.7" fill="none" stroke="#fff" stroke-width="1.6"/></svg>Flea and Tick Prevention</li>
      <li><svg width="13" height="13" viewBox="0 0 16 16"><circle cx="8" cy="8" r="7" fill="none" stroke="#fff" stroke-width="1.4"/><path d="M4.5 8.2l2.3 2.3 4.7-4.7" fill="none" stroke="#fff" stroke-width="1.6"/></svg>Heartworm Prevention</li>
      <li><svg width="13" height="13" viewBox="0 0 16 16"><circle cx="8" cy="8" r="7" fill="none" stroke="#fff" stroke-width="1.4"/><path d="M4.5 8.2l2.3 2.3 4.7-4.7" fill="none" stroke="#fff" stroke-width="1.6"/></svg>In House Laboratory</li>
      <li><svg width="13" height="13" viewBox="0 0 16 16"><circle cx="8" cy="8" r="7" fill="none" stroke="#fff" stroke-width="1.4"/><path d="M4.5 8.2l2.3 2.3 4.7-4.7" fill="none" stroke="#fff" stroke-width="1.6"/></svg>Microchipping</li>
      <li><svg width="13" height="13" viewBox="0 0 16 16"><circle cx="8" cy="8" r="7" fill="none" stroke="#fff" stroke-width="1.4"/><path d="M4.5 8.2l2.3 2.3 4.7-4.7" fill="none" stroke="#fff" stroke-width="1.6"/></svg>Nutritional Consultations</li>
      <li><svg width="13" height="13" viewBox="0 0 16 16"><circle cx="8" cy="8" r="7" fill="none" stroke="#fff" stroke-width="1.4"/><path d="M4.5 8.2l2.3 2.3 4.7-4.7" fill="none" stroke="#fff" stroke-width="1.6"/></svg>Orthopedic Surgery</li>
      <li><svg width="13" height="13" viewBox="0 0 16 16"><circle cx="8" cy="8" r="7" fill="none" stroke="#fff" stroke-width="1.4"/><path d="M4.5 8.2l2.3 2.3 4.7-4.7" fill="none" stroke="#fff" stroke-width="1.6"/></svg>Parasite Testing and Treatment</li>
      <li><svg width="13" height="13" viewBox="0 0 16 16"><circle cx="8" cy="8" r="7" fill="none" stroke="#fff" stroke-width="1.4"/><path d="M4.5 8.2l2.3 2.3 4.7-4.7" fill="none" stroke="#fff" stroke-width="1.6"/></svg>Puppy and Kitten Care</li>
      <li><svg width="13" height="13" viewBox="0 0 16 16"><circle cx="8" cy="8" r="7" fill="none" stroke="#fff" stroke-width="1.4"/><path d="M4.5 8.2l2.3 2.3 4.7-4.7" fill="none" stroke="#fff" stroke-width="1.6"/></svg>Senior Wellness</li>
      <li><svg width="13" height="13" viewBox="0 0 16 16"><circle cx="8" cy="8" r="7" fill="none" stroke="#fff" stroke-width="1.4"/><path d="M4.5 8.2l2.3 2.3 4.7-4.7" fill="none" stroke="#fff" stroke-width="1.6"/></svg>Soft Tissue Surgery</li>
      <li><svg width="13" height="13" viewBox="0 0 16 16"><circle cx="8" cy="8" r="7" fill="none" stroke="#fff" stroke-width="1.4"/><path d="M4.5 8.2l2.3 2.3 4.7-4.7" fill="none" stroke="#fff" stroke-width="1.6"/></svg>Ultrasound</li>
      <li><svg width="13" height="13" viewBox="0 0 16 16"><circle cx="8" cy="8" r="7" fill="none" stroke="#fff" stroke-width="1.4"/><path d="M4.5 8.2l2.3 2.3 4.7-4.7" fill="none" stroke="#fff" stroke-width="1.6"/></svg>Vaccinations</li>
      <li><svg width="13" height="13" viewBox="0 0 16 16"><circle cx="8" cy="8" r="7" fill="none" stroke="#fff" stroke-width="1.4"/><path d="M4.5 8.2l2.3 2.3 4.7-4.7" fill="none" stroke="#fff" stroke-width="1.6"/></svg>Wellness Exams</li>
    </ul>
    <div class="services__thumbs">
      <div class="thumb" role="img" aria-label="Photo of the hospital surgery team at work"></div>
      <div class="thumb" role="img" aria-label="Photo of a pet being examined"></div>
      <div class="thumb" role="img" aria-label="Photo of the hospital treatment room"></div>
    </div>
    <div class="services__url">www.thecorvelpets.com</div>
  </article>

  <article class="panel love">
    <h2 class="head-bar">We Love Them All</h2>
    <div class="body-text">
      <p>We have an incredible diversity of loyal four-legged and winged patients, from dogs and cats to birds, rabbits and reptiles. Every one of them is treated as family here.</p>
      <p>This is a town where animals know our names, and we know theirs. Each visit is a chance to build trust, share advice and keep your companion healthy for life.</p>
      <p>We built Bramfield Animal Hospital for you. It is our promise that every pet who walks through our doors receives gentle hands, clear answers and care you can feel good about.</p>
    </div>
    <div class="love__circles">
      <span></span>
      <div class="love__circle" role="img" aria-label="Photo of a small white dog" style="background:radial-gradient(circle,#f1ede6,#a99884)"></div>
      <div class="love__circle" role="img" aria-label="Photo of a green parrot" style="background:radial-gradient(circle,#7fc06a,#2f7a3a)"></div>
      <span></span>
    </div>
    <div class="photo photo--main" role="img" aria-label="Photo of a technician using a microscope in the hospital laboratory"></div>
    <svg class="curve" style="bottom:250px" width="367" height="60" viewBox="0 0 367 60" preserveAspectRatio="none"><path d="M0 0H367V10Q150 70 0 40Z" fill="#fff"/></svg>
  </article>
</section>

</body>
</html>
```